I need a sophisticated and powerful book cover design that combines Japanese minimalism with contemporary appeal. The cover should convey personal transformation through the metaphor of a katana (Japanese sword).
Key Design Elements:
A katana, either partially shown or artistically rendered
Subtle Japanese design elements without being stereotypical
Clean, minimalist aesthetic
Professional font selection that bridges Eastern and Western typography
Color scheme: Deep blacks, steel grays, and possibly a touch of red or gold for accent
Mood/Style:
Professional and sophisticated
Blend of traditional Japanese aesthetics with modern design
Should appeal to personal development and business readers
Must convey strength and transformation
Elegant rather than aggressive
Specific Requirements:
Title: "The Lantern Compass"
Subtitle: "Quiet Practices for Growing Inner Steadiness and Calm Endurance Daily"
Author names: Moheshan Tadeli and Veena Tadeli
Cover dimensions: Standard hardcover book size (6" x 9")
Must work well in both physical and digital thumbnail formats
Should be striking and legible when viewed as a small image online
Design Specifics:
Japanese elements such as brushstroke effects, kanji characters, or wave patterns
The design should reflect the book's core message: personal transformation through Japanese wisdom principles, using the katana as a metaphor for growth and development.
Colors
Look and feel

```html
<!DOCTYPE html>
<html lang="en">
<head>
<meta charset="utf-8">
<title>The Lantern Compass — Book Cover</title>
<link rel="stylesheet" href="https://fonts.googleapis.com/css2?family=Permanent+Marker&family=Audiowide&family=Montserrat:wght@800&display=block">
<style>
  :root {
    --paper: #ffffff;
    --ink: #0d0d0d;
    --accent: #e8202a;
    --on-accent: #ffffff;
  }
  html, body {
    margin: 0;
    padding: 0;
    overflow: hidden;
    background: var(--paper);
  }
  .cover {
    position: relative;
    width: 800px;
    height: 1200px;
    overflow: hidden;
    background: var(--paper);
  }
  .title {
    position: absolute;
    left: 0;
    top: 150px;
    width: 800px;
    margin: 0;
    text-align: center;
    font-weight: 400;
  }
  .title__lead {
    display: block;
    font-family: "Permanent Marker", "Marker Felt", "Brush Script MT", cursive;
    color: var(--ink);
    font-size: 104px;
    line-height: 1.05;
    transform: rotate(-4deg);
    margin-left: 10px;
  }
  .title__main {
    display: block;
    font-family: "Permanent Marker", "Marker Felt", "Brush Script MT", cursive;
    color: var(--accent);
    font-size: 132px;
    line-height: 1.2;
    letter-spacing: -2px;
    transform: rotate(-2deg);
  }
  .title__tail {
    display: block;
    font-family: "Audiowide", sans-serif;
    color: var(--ink);
    font-size: 50px;
    line-height: 1;
    margin-top: -4px;
    padding-left: 235px;
  }
  .slash-art {
    position: absolute;
    left: 74px;
    top: 545px;
    width: 692px;
    height: 265px;
    background: linear-gradient(160deg, var(--ink) 0%, #3a1012 55%, var(--accent) 100%);
  }
  .subtitle {
    position: absolute;
    left: 190px;
    top: 905px;
    margin: 0;
    font-family: "Audiowide", sans-serif;
    font-weight: 400;
  }
  .subtitle__lead {
    display: block;
    font-size: 19px;
    color: var(--ink);
    line-height: 1;
    margin-left: -2px;
    margin-bottom: 10px;
  }
  .subtitle__band {
    display: table;
    margin-left: 0;
    margin-bottom: 10px;
    padding: 5px 12px 4px;
    background: var(--accent);
    color: var(--on-accent);
    font-size: 19px;
    line-height: 1.1;
  }
  .authors {
    position: absolute;
    top: 815px;
    left: 652px;
    display: flex;
    gap: 14px;
    font-family: "Montserrat", sans-serif;
    font-weight: 800;
    font-size: 15px;
  }
  .author {
    margin: 0;
    writing-mode: vertical-rl;
    text-orientation: upright;
    letter-spacing: 3px;
    line-height: 1;
  }
  .author--first { margin-top: 18px; }
  .author__given { color: var(--accent); }
  .author__family { color: var(--ink); margin-top: 16px; }
  .author__joiner {
    color: var(--accent);
    font-size: 24px;
    margin-bottom: 4px;
  }
</style>
</head>
<body>
<main class="cover">
  <h1 class="title">
    <span class="title__lead">The</span>
    <span class="title__main">Lantern</span>
    <span class="title__tail">Compass</span>
  </h1>

  <div class="slash-art" role="img" aria-label="Brushstroke illustration of crossed black and red sword slashes"></div>

  <h2 class="subtitle">
    <span class="subtitle__lead">Quiet Practices for</span>
    <span class="subtitle__band">Growing Inner Steadiness and</span>
    <span class="subtitle__band">Calm Endurance Daily</span>
  </h2>

  <div class="authors">
    <p class="author author--first">
      <span class="author__given">MOHESHAN</span><span class="author__family">TADELI</span>
    </p>
    <p class="author">
      <span class="author__joiner">&amp;</span><span class="author__given">VEENA</span><span class="author__family">TADELI</span>
    </p>
  </div>
</main>
</body>
</html>
```